Complete Stationary Package for Harbor Chapel
Harbor Chapel -- The Believers of Redfield (under Harbor Chapel and smaller)
Complete Stationary Package for Harbor Chapel  - Religion and Spirituality
Creative Brief
Use specific fonts
new, vibrant, creative (please see comments below -- suprise and impress me!))
Bright & Fun-filled
Martin Delvaux
Pastor
418 W. Brinley Ave Longview, TX 75612
hcredfield@mailnest.example
harborredfield.example
I love this logo, the shape and the concept and the way the c and the t work together. However, I would like stationary designers to please use a much more creative font. Also, feel free to change, enhance the colors of the logo itself as you feel is best.
OPTION ONE Service Times Prayer Sunday 10 am Friday 7 pm Sunday 6 pm Youth Service Wednesday 7 pm Friday 8 pm OPTION TWO Harbor Chapel The Believers of Redfield www.harborredfield.example I would like to see both options if possible in order to help me decide which works best. Thanks!
kmrowell kmrowell
Please use avatars for all information such as phone, email, website, etc.
Designers: Thanks for your wonderful contributions! I have uploaded an another version of the same logo that may look a lot better against a solid background. It may be that one looks good on a white back ground, the other on a solid background. Please help me make this determination. Also, know that I am willing to provide extra compensation for extra effort. Thanks! Martin
Also, please show designs with at least a couple of different fonts. Thanks!
Clarification: The following information should read -- Services Sunday 10 am Sunday 6 pm Wednesday 7 pm Prayer Friday 7 pm Youth Service / Activities Friday 8 pm Thanks!
Thanks for the immediate response to this contest! We're off to a fantastic start! Please keep in mind that I'm looking for a complete stationary package -- folder, letterhead, envelopes, electronic signature, cd labels, etc.

```html
<!DOCTYPE html>
<html lang="en">
<head>
<meta charset="utf-8">
<title>Harbor Chapel — Business Card</title>
<link rel="stylesheet" href="https://fonts.googleapis.com/css2?family=Cinzel:wght@600&family=Open+Sans:wght@400;600&display=swap">
<style>
  :root {
    --page-bg: #eceae6;
    --card-white: #ffffff;
    --blue-light: #5fd0f0;
    --blue-deep: #1190c8;
    --green-light: #c4e48a;
    --green-deep: #6bb24a;
    --brand-orange: #e58a1f;
    --brand-blue: #1b86c2;
    --text-dark: #4a5560;
    --text-soft: #7d8790;
  }
  * { margin: 0; padding: 0; box-sizing: border-box; }
  html, body { width: 1200px; height: 696px; overflow: hidden; }
  body {
    background: var(--page-bg);
    font-family: "Open Sans", Arial, sans-serif;
    position: relative;
  }
  .card {
    position: absolute;
    top: 198px;
    width: 525px;
    height: 300px;
    background: var(--card-white);
    border-radius: 18px;
    overflow: hidden;
    box-shadow: 0 10px 28px rgba(0,0,0,0.18);
  }
  .card--front { left: 50px; }
  .card--back { left: 625px; }
  .wave { position: absolute; inset: 0; }
  .sprout-area {
    position: absolute;
    left: 24px;
    bottom: 20px;
    width: 170px;
    height: 110px;
    border-radius: 10px;
    background: linear-gradient(160deg, var(--green-light), var(--green-deep));
    opacity: 0.85;
  }
  .person { position: absolute; left: 34px; top: 52px; }
  .person__name {
    font-family: "Cinzel", Georgia, serif;
    font-weight: 600;
    font-size: 20px;
    color: var(--brand-blue);
  }
  .person__role { font-size: 12px; color: var(--text-soft); margin-top: 2px; letter-spacing: 1px; }
  .contact {
    position: absolute;
    right: 26px;
    top: 44px;
    list-style: none;
    color: #fff;
    font-size: 11.5px;
  }
  .contact li { display: flex; align-items: center; justify-content: flex-end; gap: 8px; margin-bottom: 9px; }
  .contact svg { width: 14px; height: 14px; flex: none; }
  .brand {
    position: absolute;
    left: 40px;
    top: 118px;
    display: flex;
    align-items: center;
    gap: 12px;
  }
  .brand__dot { width: 38px; height: 38px; border-radius: 50%; background: var(--brand-blue); }
  .brand__name {
    font-family: "Cinzel", Georgia, serif;
    font-weight: 600;
    font-size: 26px;
    color: var(--brand-orange);
  }
  .brand__tagline {
    position: absolute;
    left: 40px;
    top: 166px;
    font-size: 11px;
    color: var(--text-soft);
  }
  .back-details {
    position: absolute;
    left: 40px;
    top: 194px;
    font-size: 10.5px;
    color: var(--text-dark);
    line-height: 1.6;
  }
</style>
</head>
<body>

<section class="card card--front">
  <svg class="wave" viewBox="0 0 525 300" aria-hidden="true">
    <defs>
      <linearGradient id="waveFront" x1="0" y1="0" x2="1" y2="1">
        <stop offset="0" stop-color="#5fd0f0"/>
        <stop offset="1" stop-color="#1190c8"/>
      </linearGradient>
    </defs>
    <path d="M250 0 C 210 90, 300 170, 525 215 L 525 0 Z" fill="url(#waveFront)"/>
  </svg>
  <div class="sprout-area" role="img" aria-label="Green leaf sprout illustration"></div>
  <div class="person">
    <p class="person__name">Martin Delvaux</p>
    <p class="person__role">Pastor</p>
  </div>
  <ul class="contact">
    <li>418 W. Brinley Ave Longview, TX 75612
      <svg viewBox="0 0 14 14"><path d="M7 1a4 4 0 0 0-4 4c0 3 4 8 4 8s4-5 4-8a4 4 0 0 0-4-4zm0 5.5a1.5 1.5 0 1 1 0-3 1.5 1.5 0 0 1 0 3z" fill="#fff"/></svg></li>
    <li>hcredfield@mailnest.example
      <svg viewBox="0 0 14 14"><rect x="1" y="3" width="12" height="8" rx="1" fill="none" stroke="#fff" stroke-width="1.3"/><path d="M1.5 3.5 7 8l5.5-4.5" fill="none" stroke="#fff" stroke-width="1.3"/></svg></li>
    <li>www.harborredfield.example
      <svg viewBox="0 0 14 14"><circle cx="7" cy="7" r="5.5" fill="none" stroke="#fff" stroke-width="1.3"/><path d="M1.5 7h11M7 1.5c-2.5 3-2.5 8 0 11M7 1.5c2.5 3 2.5 8 0 11" fill="none" stroke="#fff" stroke-width="1"/></svg></li>
  </ul>
</section>

<section class="card card--back">
  <svg class="wave" viewBox="0 0 525 300" aria-hidden="true">
    <defs>
      <linearGradient id="waveBack" x1="0" y1="0" x2="1" y2="1">
        <stop offset="0" stop-color="#5fd0f0"/>
        <stop offset="1" stop-color="#1190c8"/>
      </linearGradient>
    </defs>
    <path d="M420 0 C 410 40, 450 75, 525 85 L 525 0 Z" fill="url(#waveBack)"/>
  </svg>
  <div class="brand">
    <span class="brand__dot"></span>
    <span class="brand__name">Harbor Chapel</span>
  </div>
  <p class="brand__tagline">Harbor Chapel -- The Believers of Redfield</p>
  <div class="back-details">
    <p>Martin Delvaux, Pastor</p>
    <p>418 W. Brinley Ave Longview, TX 75612</p>
    <p>hcredfield@mailnest.example</p>
  </div>
</section>

</body>
</html>
```